Poster Design

Hello,

My name is Rowan Pickett and I run a vidora channel called 'CrumbleDiary'. I want a poster made for those who watch my video to purchase and put on their wall at home. The poster will be all text and as you can see, I've attached a few examples of posters which I would like it to be similar to. I use a lot of the colour #ab6f7f so it would be good to incorporate this in somewhere (maybe the background colour).
I would like the poster to say:
"Do More Of What Makes YOU Happy"
I need this poster to be for sale ready for christmas, so Im going to need the designs created as soon as possible. Im sorry for the rush.
Have fun with it and feel free to upload multiple versions of a design as well as a few designs if you like.
I look forward to seeing what you come up with.
Rowan
(Of course I will need to own all rights once the payment has been made)

```html
<!DOCTYPE html>
<html lang="en">
<head>
<meta charset="utf-8">
<title>Do More Of What Makes You Happy – CrumbleDiary Poster</title>
<link rel="stylesheet" href="https://fonts.googleapis.com/css2?family=Alfa+Slab+One&family=Anton&family=Playfair+Display:wght@400&display=block">
<style>
  :root {
    --poster-rose: #ab6f7f;
    --banner-white: #ffffff;
    --type-white: #ffffff;
    --type-rose: #ab6f7f;
    --shadow-rose: rgba(90, 40, 55, 0.45);
    --rule-line: rgba(255, 255, 255, 0.55);
    --badge-rose: #94586a;
  }
  html, body {
    margin: 0;
    padding: 0;
    overflow: hidden;
    background: var(--poster-rose);
  }
  .poster {
    position: relative;
    width: 849px;
    height: 1200px;
    background: var(--poster-rose);
    overflow: hidden;
  }
  .banner-area {
    position: absolute;
    left: 150px;
    top: 66px;
    width: 549px;
    height: 150px;
    background: var(--banner-white);
    box-shadow: 4px 6px 8px var(--shadow-rose);
  }
  .banner-text {
    position: absolute;
    left: 0;
    top: 92px;
    width: 849px;
    margin: 0;
    text-align: center;
    font-family: "Playfair Display", Georgia, serif;
    font-weight: 400;
    font-size: 80px;
    line-height: 1;
    color: var(--type-rose);
  }
  .line {
    position: absolute;
    left: 0;
    width: 849px;
    margin: 0;
    text-align: center;
    color: var(--type-white);
    line-height: 1;
    text-shadow: 4px 5px 4px var(--shadow-rose);
  }
  .line-of {
    top: 272px;
    font-family: "Alfa Slab One", "Rockwell", serif;
    font-weight: 400;
    font-size: 64px;
  }
  .line-what {
    top: 346px;
    font-family: "Alfa Slab One", "Rockwell", serif;
    font-weight: 400;
    font-size: 128px;
    letter-spacing: -2px;
  }
  .divider {
    position: absolute;
    top: 518px;
    height: 2px;
    width: 210px;
    background: var(--rule-line);
  }
  .divider-left { left: 130px; }
  .divider-right { left: 509px; }
  .line-makes {
    top: 500px;
    font-family: "Playfair Display", Georgia, serif;
    font-size: 38px;
    text-shadow: none;
  }
  .line-you {
    top: 540px;
    font-family: "Anton", Impact, sans-serif;
    font-size: 200px;
    letter-spacing: 2px;
  }
  .arc-happy {
    position: absolute;
    left: 0;
    top: 0;
    filter: drop-shadow(4px 6px 4px var(--shadow-rose));
  }
  .happy-text {
    font-family: "Alfa Slab One", "Rockwell", serif;
    font-weight: 400;
    font-size: 130px;
    fill: var(--type-white);
  }
  .channel-mark {
    position: absolute;
    top: 1058px;
    left: 0;
    width: 849px;
    display: flex;
    justify-content: center;
    align-items: center;
    gap: 14px;
  }
  .channel-dot {
    width: 22px;
    height: 22px;
    border-radius: 50%;
    background: var(--badge-rose);
  }
  .channel-name {
    font-family: "Playfair Display", Georgia, serif;
    font-size: 30px;
    color: var(--type-white);
  }
</style>
</head>
<body>
<main class="poster">
  <div class="banner-area" role="img" aria-label="White ribbon banner behind the opening words"></div>
  <h1 class="banner-text">DO MORE</h1>

  <p class="line line-of">Of</p>
  <p class="line line-what">WHAT</p>

  <div class="divider divider-left"></div>
  <p class="line line-makes">MAKES</p>
  <div class="divider divider-right"></div>

  <p class="line line-you">YOU</p>

  <svg class="arc-happy" width="849" height="1000" viewBox="0 0 849 1000">
    <defs>
      <path id="happy-arc" d="M 105 945 Q 424.5 770 744 945"/>
    </defs>
    <text class="happy-text" text-anchor="middle">
      <textPath href="#happy-arc" startOffset="50%" textLength="600" lengthAdjust="spacingAndGlyphs">HAPPY</textPath>
    </text>
  </svg>

  <div class="channel-mark">
    <span class="channel-dot"></span>
    <span class="channel-name">CrumbleDiary</span>
  </div>
</main>
</body>
</html>
```